Valmoré Fine Jewelry needs a print advertisment design

Objective
Design a high impact elegant and classy print advertisment for placement in brochures and magazines and create banners with. The intent will be for the Target Audience to want to visit the physical store to want to view the bridal ring collection and make purchases. The first use will be in a brochure handed out to brides-to-be at a wedding vendor exhibition.
Format & Size: Pdf, A4 size (potrait)
* not that the edges of the ad might get trimmed for the brochure.
Overall Look & Feel
The creative suggested should align with the logo - its subtle yet distinctive style. The colours used would be a good reference to the kind of contrast colours we would like used for the print ad as well. The print must stand out from other ads that will be placed in 12 page brochure. We will not have a booth at the event to meet with potential customers like some other vendors, so we will like to really jump out to our audience that catch a glimpse of our ad in the brochure and be inclined to find more about us or share us with other people.
Target Audience
- Woman in the age group of 20 - 50 yrs
- Literate, Outgoing, Social
- English speaking
Description of Business
We are a afforable, handcrafted, high end jewelry retail store targeted at woman. The store is located in Lagos, Nigeria in a high end mall. The store offers 18karat gold jewelry with gemstones and diamonds for women, men and children - engagement rings, wedding bands, bangles, chanderlier earrings, watches, necklaces, men bracelets, baby earrings and much more. We are mostly known for our bridal jewelry: engagement ring and wedding bands. Most of our pieces and designed by us and highly skilled Italian designers and handcrafted in Italy. We offer an uncluttered highly sophisticated environment for consumers to shop at leisure. We are opened everyday, which is a great plus because there are very few luxury jewelry stores in Nigeria and fewer that are opened everyday. We love what we do and think love rocks!
The store is bright and features gold tones everywhere excuding luxury.
We also carry the world renowed Italian brands,
a) Brascelli
b) Matteo Varni
c) Lusq and so on
Social Networking
-Prominent mention of the store's Pictogram and Friendspace site encouraging Consumers to 'Like' us on FS and follow us on PG @valmorefinejewelry
Store Address & Timings
The store address and business hours of operations must be prominently mentioned.
Address: Palmcrest Arcade Mall
2nd Floor, 58 Okonkwo Adeyemi Road
Victoria Island, Lagos
Nigeria
+234-17364081, +234-8032617749
Timings: Open Everyday
Mon-Sat: 10:00am to 6:30pm, Sun: 1:00pm to 6:30pm
Photographs
We are thinking to mostly focus on our diamond engagement rings in the advert and mention the other items we carry in-store. I have attached a bunch of images of pieces in the store that we could use for the advert. I also attached a Marlowe ad I came across and like, i like the rings popping, the clean lines, identification with the marlowe colour, the play on the "Love" word and the idea the love fairy tale most women dream of.
Logo Colors & Fonts
Attached is the logo we presently use. we would like to play on these colors.
Please consider an option to include a version with a promotion sale somewhere on the flyer. Easter Sale: 20% Off all In-store Engagement rings, Wedding bands and other selected jewelry.* Date: April 1st to April 30th, 2014 *Does not apply to past purchase.
Thanx!

```html
<!DOCTYPE html>
<html lang="en">
<head>
<meta charset="utf-8">
<title>Valmoré Fine Jewelry – Easter Sale</title>
<link rel="stylesheet" href="https://fonts.googleapis.com/css2?family=Cormorant+Garamond:ital,wght@0,400;0,500;0,600;1,400&display=swap">
<style>
  :root {
    --paper: #f4f3f1;
    --paper-deep: #e4e2df;
    --ink: #5e5e5e;
    --ink-soft: #7a7a7a;
    --gold: #b8933f;
    --bar: #5b5b5b;
    --bar-text: #ececec;
  }
  * { margin: 0; padding: 0; box-sizing: border-box; }
  html, body { width: 847px; height: 1200px; overflow: hidden; }
  body { font-family: "Cormorant Garamond", Georgia, serif; color: var(--ink); }
  .ad {
    position: relative;
    width: 847px; height: 1200px;
    background: radial-gradient(ellipse at 50% 30%, #ffffff 0%, var(--paper) 45%, var(--paper-deep) 100%);
    overflow: hidden;
  }
  .backdrop-swirl {
    position: absolute; left: 0; top: 0; width: 847px; height: 620px;
    background: radial-gradient(ellipse at 30% 20%, rgba(255,255,255,0.9) 0%, rgba(255,255,255,0) 60%);
  }
  .ring-photo {
    position: absolute; left: 100px; top: 300px; width: 650px; height: 270px;
    border-radius: 50% / 50%;
    background: radial-gradient(ellipse at 50% 45%, #fdfdfd 0%, #d9d9db 45%, #bdbdc1 70%, rgba(228,226,223,0) 100%);
  }
  .offer { position: absolute; left: 0; top: 578px; width: 847px; text-align: center; }
  .offer-title { font-size: 46px; font-weight: 500; color: var(--ink); letter-spacing: 0.5px; line-height: 1.1; }
  .offer-body { margin-top: 8px; font-size: 23px; line-height: 29px; color: var(--ink); }
  .offer-body sup { font-size: 13px; }
  .offer-note { margin-top: 2px; font-size: 14px; font-style: italic; color: var(--ink-soft); }
  .store-info {
    position: absolute; left: 0; top: 722px; width: 847px; text-align: center;
    font-size: 14.5px; line-height: 26px; color: var(--ink-soft); font-style: normal;
  }
  .store-info sup { font-size: 9px; }
  .brand { position: absolute; left: 0; top: 915px; width: 847px; text-align: center; }
  .brand-name { font-size: 40px; font-weight: 500; color: var(--gold); line-height: 1.2; }
  .social-bar {
    position: absolute; left: 0; bottom: 0; width: 847px; height: 80px;
    background: var(--bar); display: flex; align-items: center; justify-content: center; gap: 50px;
    color: var(--bar-text); font-size: 19px;
  }
  .social-item { display: flex; align-items: center; gap: 12px; white-space: nowrap; }
  .social-dot { width: 24px; height: 24px; border-radius: 50%; background: var(--bar-text); }
</style>
</head>
<body>
<main class="ad">
  <div class="backdrop-swirl" role="img" aria-label="Soft white swirling light background"></div>
  <div class="ring-photo" role="img" aria-label="Photograph of stacked diamond engagement rings and wedding bands with ruby and sapphire centre stones"></div>

  <section class="offer">
    <h1 class="offer-title">Start Your Collection:</h1>
    <p class="offer-body">Easter Sale – 20% Off all In-store Engagement rings, Wedding bands<br>and other selected jewelry.* April 1<sup>st</sup> to April 30<sup>th</sup>, 2014.</p>
    <p class="offer-note">*Cannot be combined with any other offer. Not valid on previous purchases.</p>
  </section>

  <address class="store-info">
    Palmcrest Arcade Mall, 2<sup>nd</sup> Floor, 58 Okonkwo Adeyemi Road, Victoria Island, Lagos, Nigeria<br>
    +234-17364081, +234-8032617749 &nbsp;|&nbsp; Open Everyday &nbsp;|&nbsp; Mon-Sat: 10:00am to 6:30pm, Sun: 1:00pm to 6:30pm<br>
    info@valmorejewelry.com &nbsp;|&nbsp; www.valmorejewelry.com
  </address>

  <section class="brand">
    <p class="brand-name">Valmoré Fine Jewelry</p>
  </section>

  <footer class="social-bar">
    <div class="social-item"><span class="social-dot"></span>Like us on Friendspace: valmorefinejewelry</div>
    <div class="social-item"><span class="social-dot"></span>Follow us on Pictogram: valmorefinejewelry</div>
  </footer>
</main>
</body>
</html>
```